Business card design for Plumbing and Gas fitting company

We need a business card design for our plumbing and gas fitting company using the company logo and director details. Design should be modern and eye-catching however kept reasonably simple. This design should be targeted at commercial businesses/work so professionalism is key.

Target Market(s)

Commercial/business

Industry/Entity Type

Plumbing

Contact Information for Business Card

Warren Dohey
Director
027 581 9043
warren@vantorplumbingandgas.example
PO Box 7816
Palmerston North 4472

Font styles to use
Sans Serif

Requirements
Must have
• Logo
• Modern
• Kept simple
Nice to have
• Colour scheme based around logo

```html
<!DOCTYPE html>
<html lang="en">
<head>
<meta charset="utf-8">
<title>Vantor Plumbing &amp; Gas — Business Card</title>
<link rel="stylesheet" href="https://fonts.googleapis.com/css2?family=Open+Sans:wght@400;600;700&display=swap">
<style>
  :root {
    --stage: #000000;
    --card-front: #f3f3f3;
    --brand-blue: #1a6fb8;
    --brand-orange: #e8792b;
    --text-dark: #2b2b2b;
    --back-blue: #0b78c8;
    --back-blue-deep: #066bb8;
    --white: #ffffff;
  }
  * { box-sizing: border-box; margin: 0; padding: 0; }
  html, body {
    width: 1200px; height: 900px; overflow: hidden;
    background: var(--stage);
    font-family: "Open Sans", Arial, sans-serif;
  }
  .stage { position: relative; width: 1200px; height: 900px; }

  .card {
    position: absolute; top: 200px;
    width: 310px; height: 502px;
  }
  .card--front {
    left: 265px;
    background: var(--card-front);
    border-radius: 62px 0 62px 0;
  }
  .card--back {
    left: 641px; width: 309px;
    background: linear-gradient(160deg, var(--back-blue) 0%, var(--back-blue-deep) 100%);
    border-radius: 0 62px 0 62px;
    display: flex; flex-direction: column; align-items: center; justify-content: center;
  }

  .brand-name {
    position: absolute; left: 26px; top: 370px;
    font-size: 21px; font-weight: 700; color: var(--brand-blue);
    letter-spacing: -0.2px; white-space: nowrap;
    top: 175px;
  }

  .contact {
    position: absolute; left: 24px; top: 318px;
    color: var(--text-dark); font-size: 13.5px; line-height: 18px;
  }
  .contact__name {
    font-size: 17.5px; font-weight: 400; line-height: 22px;
    color: var(--brand-blue); text-transform: uppercase;
  }
  .contact__name .surname { color: var(--brand-orange); }
  .contact__role { margin-bottom: 10px; }
  .contact__address { margin-bottom: 8px; }
  .contact__line { display: flex; align-items: center; gap: 5px; }
  .contact__line svg { width: 11px; height: 11px; fill: var(--brand-blue); flex: none; }

  .back-name {
    color: var(--white); font-size: 22px; font-weight: 700;
    text-align: center; line-height: 28px; max-width: 220px;
  }
  .back-dot {
    width: 64px; height: 64px; border-radius: 50%;
    background: var(--white); margin-bottom: 18px;
  }
</style>
</head>
<body>
<main class="stage">
  <section class="card card--front">
    <div class="brand-name">Vantor Plumbing &amp; Gas</div>

    <div class="contact">
      <div class="contact__name">Warren <span class="surname">Dohey</span></div>
      <div class="contact__role">Director</div>
      <div class="contact__address">PO Box 7816<br>Palmerston North 4472</div>
      <div class="contact__line">
        <svg viewBox="0 0 24 24" aria-hidden="true"><path d="M6.6 10.8a15.1 15.1 0 0 0 6.6 6.6l2.2-2.2c.3-.3.7-.4 1-.2 1.1.4 2.3.6 3.6.6.6 0 1 .4 1 1V20c0 .6-.4 1-1 1A17 17 0 0 1 3 4c0-.6.4-1 1-1h3.5c.6 0 1 .4 1 1 0 1.3.2 2.5.6 3.6.1.3 0 .7-.2 1z"/></svg>
        <span>027 581 9043</span>
      </div>
      <div class="contact__line">
        <svg viewBox="0 0 24 24" aria-hidden="true"><path d="M2 5h20v14H2z M2 5l10 8 10-8" /><path d="M3 6.5l9 7 9-7V18H3z" fill="var(--card-front)"/><path d="M2 5h20v2l-10 7L2 7z" fill="var(--brand-blue)"/></svg>
        <span>warren@vantorplumbingandgas.example</span>
      </div>
    </div>
  </section>

  <section class="card card--back" role="img" aria-label="Blue card back with soft wave pattern and brand name">
    <div class="back-dot"></div>
    <div class="back-name">Vantor Plumbing &amp; Gas</div>
  </section>
</main>
</body>
</html>
```